Harbor Vantage needs new design business card

We are video surveillance and analytics software development company.
I am looking for a professional business card.
Our website is www.harborvantage-example.com.au
Please have a loo and get the feel for who we are and what we do.
I do not know what else to give you apart from good luck and I hope your design gets selected.
Thank you very much for participating
Industry/Entity Type
Business
Contact Information for Business Card
Address
27/14 Pemberly Street Millbrook NSW 2199
Telephone 1300 582 741
Mobile 0450 713 258
email: marcus@harborvantage-example.com.au
name
Marcus Felder
Position
Managing Director
Font styles to use
Other font styles liked:
- Arial
Look and feel

```html
<!DOCTYPE html>
<html lang="en">
<head>
<meta charset="utf-8">
<title>Harbor Vantage – Business Card</title>
<link rel="stylesheet" href="https://fonts.googleapis.com/css2?family=Lato:wght@400;700;900&display=swap">
<style>
  :root {
    --navy: #1b3f6e;
    --orange: #f39220;
    --slate: #5f7a8b;
    --ink: #1a1a1a;
    --muted: #5a6f80;
    --paper: #ffffff;
    --backdrop: #e4e6e8;
  }
  * { box-sizing: border-box; margin: 0; padding: 0; }
  html, body {
    width: 1200px; height: 926px; overflow: hidden;
    background: var(--backdrop);
    font-family: "Lato", Arial, sans-serif;
  }
  .sheet {
    width: 1200px; height: 926px;
    display: flex; flex-direction: column; align-items: center; justify-content: center;
    gap: 36px;
  }
  .card {
    position: relative;
    width: 740px; height: 420px;
    overflow: hidden;
    box-shadow: 0 6px 18px rgba(0,0,0,.18);
  }
  .card--front { background: var(--paper); }
  .card--back { background: var(--navy); }
  .card__art { position: absolute; inset: 0; width: 100%; height: 100%; }

  .brand {
    position: absolute; display: flex; align-items: center; gap: 12px;
    font-weight: 900; text-transform: uppercase; letter-spacing: 1px;
  }
  .brand__mark { display: block; }
  .card--front .brand { top: 46px; left: 0; right: 0; justify-content: center; color: var(--navy); font-size: 34px; }
  .card--front .brand__mark { width: 30px; height: 30px; background: var(--navy); }
  .card--back .brand { top: 150px; left: 0; right: 0; justify-content: center; color: var(--paper); font-size: 52px; }
  .card--back .brand__mark { width: 44px; height: 44px; background: var(--paper); }

  .person { position: absolute; top: 160px; left: 60px; width: 230px; text-align: right; }
  .person__name { color: var(--orange); font-weight: 900; font-size: 26px; text-transform: uppercase; line-height: 1.1; }
  .person__role { color: var(--ink); font-weight: 700; font-size: 14px; margin-top: 2px; }

  .divider { position: absolute; top: 158px; left: 306px; width: 1px; height: 96px; background: #9aa6b0; }

  .contact { position: absolute; top: 160px; left: 322px; list-style: none; color: var(--muted); font-size: 19px; }
  .contact__item { display: flex; align-items: center; gap: 10px; height: 30px; }
  .contact__icon { width: 17px; height: 17px; fill: var(--navy); flex: none; }

  .address {
    position: absolute; left: 24px; top: 316px;
    color: var(--paper); font-size: 17px; letter-spacing: .3px;
    transform: rotate(7deg); transform-origin: left center;
  }

  .website {
    position: absolute; top: 262px; left: 0; right: 0; text-align: center;
    color: #6f8aa6; font-size: 15px; letter-spacing: 6px; text-transform: uppercase;
  }
</style>
</head>
<body>
<main class="sheet">

  <section class="card card--front" aria-label="Card front">
    <svg class="card__art" viewBox="0 0 740 420" aria-hidden="true">
      <path d="M0 228 C170 252 340 318 520 396 C350 350 170 300 0 274 Z" fill="var(--orange)"/>
      <path d="M0 286 C170 310 360 372 740 388 L740 420 L0 420 Z" fill="var(--navy)"/>
      <path d="M420 420 L740 318 L740 420 Z" fill="var(--slate)"/>
    </svg>

    <div class="brand"><span class="brand__mark"></span>Harbor Vantage</div>

    <div class="person">
      <p class="person__name">Marcus Felder</p>
      <p class="person__role">Position Managing Director</p>
    </div>

    <span class="divider"></span>

    <ul class="contact">
      <li class="contact__item">
        <svg class="contact__icon" viewBox="0 0 24 24"><path d="M3 9c0-3 4-5 9-5s9 2 9 5v2h-5V8.5c-2-.7-6-.7-8 0V11H3zM6 12h12l2 8H4z"/></svg>
        1300 582 741
      </li>
      <li class="contact__item">
        <svg class="contact__icon" viewBox="0 0 24 24"><path d="M2 5h20v14H2z M3 6l9 7 9-7" /></svg>
        0450 713 258
      </li>
      <li class="contact__item">
        <svg class="contact__icon" viewBox="0 0 24 24"><path d="M7 1h10a2 2 0 0 1 2 2v18a2 2 0 0 1-2 2H7a2 2 0 0 1-2-2V3a2 2 0 0 1 2-2zm0 3v14h10V4z"/></svg>
        marcus@harborvantage-example.com.au
      </li>
    </ul>

    <p class="address">27/14 Pemberly Street Millbrook NSW 2199</p>
  </section>

  <section class="card card--back" aria-label="Card back">
    <div class="brand"><span class="brand__mark"></span>Harbor Vantage</div>
    <p class="website">www.harborvantage-example.com.au</p>
  </section>

</main>
</body>
</html>
```